Brellow Gateworks garage door installation service and repairs

I need a business card design for my company that is called Brellow Gateworks, I install, service, repair and automate garaged doors.
I want my card to look simple and neat but I also want the information such as contact number, email address and website to be clear and noticeable. I would love a simple logo if possible, I would like to see the color blue in the card but not overpowering.

Industry/Entity Type

Garage

```html
<!DOCTYPE html>
<html lang="en">
<head>
<meta charset="utf-8">
<title>Brellow Gateworks — Business Card</title>
<link rel="stylesheet" href="https://fonts.googleapis.com/css2?family=Archivo+Black&family=Cormorant+Garamond:ital,wght@1,700&display=swap">
<style>
  :root {
    --brand-blue: #0b3566;
    --ink: #111111;
    --muted: #666666;
    --paper: #ffffff;
  }
  html, body {
    margin: 0;
    padding: 0;
    overflow: hidden;
    background: var(--paper);
  }
  .card {
    position: relative;
    width: 1200px;
    height: 685px;
    background: var(--paper);
    overflow: hidden;
    font-family: "Archivo Black", sans-serif;
  }
  .brand-mark {
    position: absolute;
    left: 140px;
    top: 55px;
    width: 150px;
    height: 150px;
    background: var(--brand-blue);
  }
  .brand-name {
    position: absolute;
    left: 391px;
    top: 40px;
    margin: 0;
    color: var(--brand-blue);
    font-family: "Archivo Black", sans-serif;
    font-weight: 400;
    font-size: 72px;
    line-height: 86px;
    letter-spacing: 0.06em;
  }
  .brand-name span { display: block; }
  .tagline {
    position: absolute;
    left: 89px;
    top: 206px;
    width: 1012px;
    margin: 0;
    color: var(--ink);
    font-family: "Cormorant Garamond", serif;
    font-style: italic;
    font-weight: 700;
    font-size: 33px;
    letter-spacing: 0.13em;
    white-space: nowrap;
  }
  .person-name {
    position: absolute;
    left: 102px;
    top: 330px;
    margin: 0;
    color: var(--ink);
    font-size: 40px;
    letter-spacing: 0.08em;
  }
  .person-role {
    position: absolute;
    left: 225px;
    top: 400px;
    margin: 0;
    color: var(--muted);
    font-size: 30px;
    letter-spacing: 0.08em;
  }
  .contact {
    position: absolute;
    left: 582px;
    top: 462px;
    margin: 0;
    padding: 0;
    list-style: none;
    color: var(--ink);
    font-size: 27px;
    letter-spacing: 0.09em;
  }
  .contact li {
    display: flex;
    height: 57px;
    align-items: center;
  }
  .contact .label {
    width: 111px;
  }
  .contact .web {
    letter-spacing: 0.14em;
  }
</style>
</head>
<body>
  <main class="card">
    <div class="brand-mark" aria-hidden="true"></div>
    <h1 class="brand-name"><span>Brellow</span><span>Gateworks</span></h1>
    <p class="tagline">install, service, repair &amp; automate garage doors</p>

    <p class="person-name">Dale&nbsp;&nbsp;????????</p>
    <p class="person-role">Proprietor</p>

    <ul class="contact">
      <li><span class="label">T&nbsp;:</span><span class="value">0491 570 156</span></li>
      <li><span class="label">@&nbsp;:</span><span class="value">dale@brellowgw.com</span></li>
      <li><span class="web">www.brellowgw.com.au</span></li>
    </ul>
  </main>
</body>
</html>
```